Summit Grading a Masonry LLC business card

My current business card is very plain. it has my logo and contact information. I woud like something that stands out from the rest. please take a look at my website to see about my company.

Compayt Name - Summit Grading And Masonry
Owner - Martin Galloway
Business Address
Business Website - www.summitgradingandmasonry.example
Email - Summitgradingandmasonry@mailbox.example
Phone - 555-214-3867
Fax - 555-630-2719

Target Market(s)

Everyone age tang is 18 - 85

Industry/Entity Type

Business

Contact Information for Business Card

Nice and professional all in one.

Font styles to use
Serif
Other font styles liked:
• Up to you

Requirements
Must have
• All contact info. The design is up to you.
Nice to have
• All the contact info the design is up to you
Should not have
• I don't have any

```html
<!DOCTYPE html>
<html lang="en">
<head>
<meta charset="utf-8">
<title>Summit Grading &amp; Masonry — Business Card</title>
<link rel="stylesheet" href="https://fonts.googleapis.com/css2?family=Questrial&display=swap">
<style>
  :root {
    --brand-red: #b8222d;
    --brand-red-dark: #9e1c26;
    --paper: #ffffff;
    --backdrop: #f1f1f1;
    --ink-light: #ffffff;
    --card-shadow: rgba(0, 0, 0, 0.18);
  }
  * { box-sizing: border-box; margin: 0; padding: 0; }
  html, body {
    width: 1200px; height: 798px; overflow: hidden;
    background: var(--backdrop);
    font-family: "Questrial", "Century Gothic", sans-serif;
  }
  .sheet {
    position: relative; width: 1200px; height: 798px;
    display: flex; align-items: center; justify-content: center; gap: 40px;
  }
  .card {
    position: relative; width: 540px; height: 309px;
    background: var(--paper);
    box-shadow: 0 6px 18px var(--card-shadow);
    overflow: hidden;
  }
  /* Front */
  .card-front { display: flex; align-items: center; justify-content: center; }
  .brand { display: flex; align-items: center; gap: 12px; }
  .brand-mark { width: 22px; height: 22px; background: var(--brand-red); }
  .brand-name { color: var(--brand-red); font-size: 30px; line-height: 1.1; }
  /* Back */
  .card-back { background: var(--brand-red); }
  .back-brand {
    position: absolute; left: 22px; top: 62px;
    display: flex; align-items: center; gap: 8px;
  }
  .back-brand .brand-mark { width: 14px; height: 14px; background: var(--ink-light); }
  .back-brand .brand-name { color: var(--ink-light); font-size: 18px; }
  .contact {
    position: absolute; right: 18px; top: 16px; text-align: right;
    color: var(--ink-light); font-size: 11px; line-height: 1.45;
  }
  .contact-name { font-size: 18px; line-height: 1.1; }
  .contact-role { font-style: italic; font-size: 11px; margin-bottom: 14px; }
  .contact-row span + span { margin-left: 12px; }
  .photo { position: absolute; bottom: 0; }
  .photo-driveway { left: 0; top: 180px; width: 232px;
    background: linear-gradient(180deg, #5f7a4e 0%, #8e9197 45%, #a9adb2 100%); }
  .photo-lot { left: 232px; top: 170px; width: 162px;
    background: linear-gradient(180deg, #7fa0c4 0%, #5a7c46 35%, #56595e 60%, #9a9c9f 100%); }
  .photo-path { left: 394px; top: 160px; width: 146px;
    background: linear-gradient(180deg, #6e8f57 0%, #4d6b3c 45%, #2f3135 70%, #3c3e42 100%); }
</style>
</head>
<body>
  <main class="sheet">
    <section class="card card-front" aria-label="Card front">
      <div class="brand">
        <span class="brand-mark"></span>
        <span class="brand-name">Summit Grading<br>&amp; Masonry</span>
      </div>
    </section>

    <section class="card card-back" aria-label="Card back">
      <div class="back-brand">
        <span class="brand-mark"></span>
        <span class="brand-name">Summit Grading<br>&amp; Masonry</span>
      </div>

      <div class="contact">
        <p class="contact-name">Martin Galloway</p>
        <p class="contact-role">Owner</p>
        <p class="contact-row"><span>Phone: 555-214-3867</span><span>Fax: 555-630-2719</span></p>
        <p>418 Ridge Avenue, Fairview, NY</p>
        <p>www.summitgradingandmasonry.example</p>
        <p>Summitgradingandmasonry@mailbox.example</p>
      </div>

      <div class="photo photo-driveway" role="img" aria-label="Photo of a freshly paved driveway in front of a garage"></div>
      <div class="photo photo-lot" role="img" aria-label="Photo of a parking lot being paved with work vehicles"></div>
      <div class="photo photo-path" role="img" aria-label="Photo of a new asphalt path beside a lawn and fence"></div>
    </section>
  </main>
</body>
</html>
```